Residential Construction Business - Site Signage

I need a design made for a site fence banner. We have a logo and branding so the design would need to be aligned with this. It would need to be made to specific size ratio so that it can be sent to the maker for production.
ratio : 4600 wide x 1700 high
The design should feature our website and also the slogan
"don't move, re-imagine"

Target Market(s)

potential clients

Industry/Entity Type

construction

Font styles to use
Other font styles liked:
• to match branding

Colors
0054AA
0677BA
7BADD7
CADEEF
E8F1F8

Requirements
Must have
• www.velmbuild.com.au Majority of the sign is our brand logo
Nice to have
• Majority of the sign is our brand logo
Should not have
• colors and themes that arent brand relevant

```html
<!DOCTYPE html>
<html lang="en">
<head>
<meta charset="utf-8">
<title>Velm Build – Site Fence Banner</title>
<link rel="stylesheet" href="https://fonts.googleapis.com/css2?family=Montserrat:wght@300;400;700&family=Work+Sans:wght@700&display=swap">
<style>
  :root {
    --navy: #023c5e;
    --white: #ffffff;
    --photo-light: #f3f3f2;
    --photo-mid: #e9e6e1;
    --photo-warm: #e6d2b4;
  }
  html, body {
    margin: 0;
    padding: 0;
    overflow: hidden;
    background: var(--white);
  }
  .banner {
    position: relative;
    width: 1200px;
    height: 444px;
    overflow: hidden;
    background: var(--white);
  }
  .interior-photo {
    position: absolute;
    inset: 0;
    background:
      radial-gradient(ellipse 320px 120px at 960px 400px, rgba(230, 210, 180, 0.55), transparent 70%),
      linear-gradient(90deg, var(--white) 40%, var(--photo-light) 70%, var(--photo-mid) 100%);
  }
  .chevron-panel {
    position: absolute;
    inset: 0;
  }
  .slogan {
    position: absolute;
    left: 153px;
    top: 62px;
    margin: 0;
    font-family: "Work Sans", sans-serif;
    font-weight: 700;
    font-size: 66px;
    line-height: 62px;
    letter-spacing: -0.3px;
    color: var(--white);
  }
  .phone {
    position: absolute;
    right: 154px;
    top: 66px;
    margin: 0;
    font-family: "Montserrat", sans-serif;
    font-weight: 300;
    font-size: 31px;
    color: var(--navy);
  }
  .brand-name {
    position: absolute;
    right: 154px;
    top: 262px;
    margin: 0;
    font-family: "Montserrat", sans-serif;
    font-weight: 700;
    font-size: 72px;
    line-height: 72px;
    letter-spacing: 1px;
    color: var(--navy);
  }
  .website {
    position: absolute;
    right: 154px;
    top: 340px;
    margin: 0;
    font-family: "Montserrat", sans-serif;
    font-weight: 400;
    font-size: 34px;
    letter-spacing: 2.2px;
    color: var(--navy);
  }
</style>
</head>
<body>
  <main class="banner">
    <div class="interior-photo" role="img" aria-label="Bright renovated open-plan living room with kitchen, dining table and sofa, washed in white"></div>

    <svg class="chevron-panel" width="1200" height="444" viewBox="0 0 1200 444" aria-hidden="true">
      <path fill="var(--navy)" d="M0 0 H690 L448 280 Q432 302 450 322 L550 444 H0 Z"/>
    </svg>

    <h1 class="slogan">don't move,<br>re-imagine</h1>
    <p class="phone">(+61) 400 183 527</p>
    <p class="brand-name">VELM BUILD</p>
    <p class="website">www.velmbuild.com.au</p>
  </main>
</body>
</html>
```